Retail healthy snack bar design

We are launching a new product range to be sold in health food stores.

The Vorla Co (no logo as yet).

We will have a range of bars, spreads (jars), shakes (bags) in the following ranges-
milk protein
plant protein
keto

For this project, please do a bar design. The chosen designer will be given additional work for the rest of the packaging as well as promotional material such as social media, banners, posters etc.

Brisk Stick Protein - Must be White to be recognized.
Brisk Stick Collagen - Bronze
Brisk Keto Stick - Possibly Red
Brisk Stick Plant - Green

Food images can be added but their must be samples without as we may need to remove for certain countries.

Target Market(s)

Healthy, Weight-loss, Bodybuilding, Elderly, Medical

Industry/Entity Type

Health And Wellness

Font styles to use
Sans Serif

Colors

Designer to choose colors to be used in the design.

Requirements
Must have
• Clean simple to read design with minimal colours

Flavour to be easily read (Must include the word 'Flavour' in the same size font as the flavour description)

Must show size of bar (60g).

Some details that can be added (optional)-
raw, cold pressed bar with (example) whey protein isolate + prebiotic fibre
natural, with no artificial colours, flavours, preservatives or sweeteners
no added sugar or sugar alcohols - gluten free - soy free

Rear of bar shall remain the same or all same details if redesigned.
Nice to have
• Clean design, use of silver foil and/or matt/gloss affect, large oversized flavour image (if including).

See images of current designs I like on the market for ideas
Should not have
• Too many images (if any).

```html
<!DOCTYPE html>
<html lang="en">
<head>
<meta charset="utf-8">
<title>Brisk Stick Protein – Vanilla Bar Wrapper</title>
<link rel="stylesheet" href="https://fonts.googleapis.com/css2?family=Open+Sans:wght@400;700;800&display=swap">
<style>
  :root {
    --stage: #272727;
    --wrapper: #f1f1f2;
    --decor-light: #ececee;
    --decor-dark: #d6d6d9;
    --ink: #111111;
    --brand-orange: #ff5a00;
    --flavour-blue: #1f3dff;
    --accent-cyan: #2bfcf8;
    --white: #ffffff;
  }
  html, body {
    margin: 0;
    width: 1200px;
    height: 857px;
    overflow: hidden;
    background: var(--stage);
  }
  .canvas {
    position: relative;
    width: 1200px;
    height: 857px;
    font-family: "Open Sans", sans-serif;
  }
  .wrapper-art {
    position: absolute;
    inset: 0;
  }
  .flavour {
    position: absolute;
    left: 770px;
    top: 292px;
    width: 145px;
    margin: 0;
    text-align: right;
    color: var(--white);
    font-weight: 700;
    font-size: 21px;
    line-height: 27px;
  }
  .brand-name {
    position: absolute;
    left: 360px;
    top: 378px;
    width: 400px;
    margin: 0;
    text-align: center;
    color: var(--brand-orange);
    font-weight: 800;
    font-size: 48px;
    line-height: 54px;
  }
  .claims {
    position: absolute;
    left: 300px;
    top: 513px;
    margin: 0;
    color: var(--ink);
    font-size: 20px;
    line-height: 26px;
    font-weight: 400;
    white-space: nowrap;
  }
  .weight {
    position: absolute;
    left: 834px;
    top: 497px;
    width: 74px;
    height: 62px;
    border: 1px solid #333;
    border-radius: 50%;
    display: flex;
    align-items: center;
    justify-content: center;
    color: var(--ink);
    font-size: 29px;
    font-weight: 400;
    box-sizing: border-box;
  }
  .weight small { font-size: 17px; margin-top: 10px; }
</style>
</head>
<body>
<main class="canvas">
  <svg class="wrapper-art" width="1200" height="857" viewBox="0 0 1200 857">
    <defs>
      <clipPath id="wrapper-clip">
        <path d="M200 275 H995 L1010 290 L995 305 L1010 320 L995 335 L1010 350 L995 365 L1010 380 L995 395 L1010 410 L995 425 L1010 440 L995 455 L1010 470 L995 485 L1010 500 L995 515 L1010 530 L995 545 L1010 560 L995 575 H200 L186 560 L200 545 L186 530 L200 515 L186 500 L200 485 L186 470 L200 455 L186 440 L200 425 L186 410 L200 395 L186 380 L200 365 L186 350 L200 335 L186 320 L200 305 L186 290 Z"/>
      </clipPath>
      <radialGradient id="decor-fill" cx="0.5" cy="0.5" r="0.5">
        <stop offset="0" stop-color="var(--decor-dark)"/>
        <stop offset="1" stop-color="var(--wrapper)"/>
      </radialGradient>
    </defs>
    <g clip-path="url(#wrapper-clip)">
      <rect class="wrapper-body" x="180" y="270" width="840" height="310" fill="var(--wrapper)"/>
      <ellipse class="decor-area" role="img" aria-label="Decorative grey swoosh graphic behind the product name" cx="430" cy="420" rx="170" ry="150" fill="url(#decor-fill)"/>
      <polygon class="band-cyan" points="697,275 730,275 1010,512 1010,522" fill="var(--accent-cyan)"/>
      <polygon class="band-orange" points="730,275 765,275 1010,495 1010,512" fill="var(--brand-orange)"/>
      <polygon class="band-blue" points="765,275 1010,275 1010,495" fill="var(--flavour-blue)"/>
    </g>
  </svg>

  <p class="flavour">VANILLA<br>FLAVOUR</p>
  <h1 class="brand-name">Brisk Stick<br>Protein</h1>
  <p class="claims">no added sugar, sugar alcohols, gluten free, soy free</p>
  <div class="weight">60<small>g</small></div>
</main>
</body>
</html>
```